New Business Card Design Project

I need a meaningful new business card. Therefore, the website should convey growth, joy, uniqueness, workout and a bit of luxury.
Color scheme should be petrol, gold and matching colors.

```html
<!DOCTYPE html>
<html lang="de">
<head>
<meta charset="utf-8">
<title>Kernwerk Studio – Visitenkarte</title>
<link rel="stylesheet" href="https://fonts.googleapis.com/css2?family=Montserrat:wght@800&family=Open+Sans:wght@400;600&display=swap">
<style>
  :root {
    --stage: #232323;
    --petrol: #17ab9f;
    --petrol-deep: #0f8479;
    --card-dark: #242427;
    --band-mid: #1e1e21;
    --band-low: #19191c;
    --text-light: #f2f2f2;
    --text-muted: #6e6e73;
  }
  * { margin: 0; padding: 0; box-sizing: border-box; }
  html, body { width: 1200px; height: 780px; overflow: hidden; background: var(--stage); }
  .stage {
    position: relative; width: 1200px; height: 780px;
    display: flex; justify-content: center; align-items: center; gap: 70px;
  }
  .card {
    position: relative; width: 330px; height: 560px; border-radius: 22px; overflow: hidden;
  }

  /* Front */
  .card-front { background: var(--petrol); display: flex; align-items: center; justify-content: center; }
  .front-mark { position: relative; width: 240px; height: 240px; display: flex; align-items: center; justify-content: center; }
  .front-mark .mark-ring { position: absolute; inset: 0; border: 2px solid var(--petrol-deep); border-radius: 50%; }
  .brand-name {
    font-family: "Open Sans", sans-serif; font-weight: 600; font-size: 26px;
    color: var(--petrol-deep); text-align: center; line-height: 1.15; letter-spacing: 0.5px;
  }

  /* Back */
  .card-back { background: var(--card-dark); }
  .back-bands { position: absolute; inset: 0; }
  .back-mark {
    position: absolute; top: 40px; left: 50%; transform: translateX(-50%);
    width: 170px; height: 170px; display: flex; align-items: center; justify-content: center;
  }
  .back-mark .mark-ring { position: absolute; inset: 0; border: 2px solid var(--petrol); border-radius: 50%; }
  .back-mark .brand-name { color: var(--petrol); font-size: 22px; }
  .person { position: absolute; top: 248px; width: 100%; text-align: center; }
  .person-name {
    font-family: "Montserrat", sans-serif; font-weight: 800; font-size: 29px; color: var(--petrol);
    line-height: 1;
  }
  .person-role {
    font-family: "Open Sans", sans-serif; font-size: 13.5px; color: var(--text-muted); margin-top: 4px;
  }
  .contact-icons { display: flex; justify-content: center; gap: 8px; margin-top: 14px; }
  .contact-icons svg { width: 26px; height: 26px; }
  .contact-list {
    list-style: none; margin-top: 10px;
    font-family: "Open Sans", sans-serif; font-size: 13.5px; color: var(--text-light); line-height: 1.4;
  }
  .social {
    position: absolute; bottom: 46px; width: 100%; text-align: center;
    font-family: "Open Sans", sans-serif; font-size: 14px; color: var(--text-light);
  }
  .social-dot {
    display: block; width: 24px; height: 24px; border-radius: 50%; background: var(--petrol);
    margin: 0 auto 8px;
  }
</style>
</head>
<body>
<main class="stage">

  <section class="card card-front" aria-label="Kartenvorderseite">
    <div class="front-mark">
      <span class="mark-ring"></span>
      <p class="brand-name">Kernwerk<br>Studio</p>
    </div>
  </section>

  <section class="card card-back" aria-label="Kartenrückseite">
    <svg class="back-bands" viewBox="0 0 330 560" preserveAspectRatio="none" aria-hidden="true">
      <path d="M0 445 C 120 470 250 440 330 360 L330 560 L0 560 Z" fill="var(--band-mid)"/>
      <path d="M0 460 C 60 470 110 455 160 430 C 220 400 280 410 330 440 L330 560 L0 560 Z" fill="var(--band-low)"/>
    </svg>

    <div class="back-mark">
      <span class="mark-ring"></span>
      <p class="brand-name">Kernwerk<br>Studio</p>
    </div>

    <div class="person">
      <h1 class="person-name">Marlene Okafor</h1>
      <p class="person-role">Pilates Studio Trainerin</p>

      <div class="contact-icons">
        <svg viewBox="0 0 26 26" aria-label="Telefon" role="img">
          <circle cx="13" cy="13" r="13" fill="var(--petrol)"/>
          <path d="M9 7.5 l2 0 1 3 -1.4 1.2 a8 8 0 0 0 3.7 3.7 l1.2-1.4 3 1 0 2 a1.5 1.5 0 0 1-1.6 1.4 A10 10 0 0 1 7.6 9.1 1.5 1.5 0 0 1 9 7.5 Z" fill="#fff"/>
        </svg>
        <svg viewBox="0 0 26 26" aria-label="E-Mail" role="img">
          <circle cx="13" cy="13" r="13" fill="var(--petrol)"/>
          <rect x="7" y="8.5" width="12" height="9" rx="1" fill="#fff"/>
          <path d="M7.5 9.5 L13 13.5 L18.5 9.5" stroke="var(--petrol)" stroke-width="1.3" fill="none"/>
        </svg>
        <svg viewBox="0 0 26 26" aria-label="Webseite" role="img">
          <circle cx="13" cy="13" r="13" fill="var(--petrol)"/>
          <circle cx="13" cy="13" r="6" fill="none" stroke="#fff" stroke-width="1.4"/>
          <ellipse cx="13" cy="13" rx="2.6" ry="6" fill="none" stroke="#fff" stroke-width="1.2"/>
          <path d="M7 13 H19" stroke="#fff" stroke-width="1.2"/>
        </svg>
      </div>

      <ul class="contact-list">
        <li>+49 160 5550182</li>
        <li>info@kernwerk-studio.de</li>
        <li>www.kernwerk-studio.de</li>
      </ul>
    </div>

    <p class="social"><span class="social-dot"></span>kernwerk_movement</p>
  </section>

</main>
</body>
</html>
```